Spa Resort Website

UPDATE:
Note that for the home page we are intending to have a slideshow showcasing elements of the resort, as per:
* www.brackenwellpools.co.nz
* www.velanira.com
* www.wanderlofty-journeys.com
We also need to know how you intend to use the colours to denote subsections, as per the brief below.
Also...the sliders denoting Elegant vs Bold etc seem to have lost their settings. I have reset them to how I believe we set them a couple of weeks ago, but there may be minor differences.
=============================================
We are developing a website for Taupo Kelmarsh, a resort in Taupo, New Zealand.
While we have been provided with a site layout and basic colour scheme, the implementation of this design does not meet the client's needs for a modern, inviting looking site.
We require a designer to work within the outline structure of the site and provide design elements to lift the design. We envisage that these design elements would include styling of the menus, building of the colour schemes from the base colours, home page design.
If you are unsure of the parameters please post a question indicating elements you would like to change and we can comment on feasibility.
We have attached the original design concept and some of the wire framing that we developed from that.
The site has four major sections, each requiring its own, subtly different, colour scheme - these schemes are to be based on the colours in the client's logo (attached). Obviously there does need to be consistency in the colour schemes across the site. The colours from the logo apply as follows:
* Stay (accommodation) - "Orange"
* Soak (Hot Springs and water park) - "Green"
* Soothe (Spa Resort) - "Beige"
* Savour (Summary of experience) - "Choc Brown"
We require the design for 2 pages:
* Home
* Detail Page (eg Family Accommodation)
Design must be flexible in that if we decide at a later date to add another block to the RH area (for example) we are able to while maintaining the integrity of the design.
Menu items include dropdowns.
We are not happy with the current layout of the HOME page and require a full redesign of this.
The resort is 5 star, but also offers camping facilities. The design therefore needs to reflect the high quality of the resort, while also being accessible to those on a budget.
The following sites can be considered reference sites for the look and feel we are seeking:
* www.brackenwellpools.co.nz
* www.velanira.com
Final deliverable is preferred in layered PNG, but .eps is acceptable. .ai is not acceptable.

```html
<!DOCTYPE html>
<html lang="en">
<head>
<meta charset="utf-8">
<title>Family Accommodation – Taupo Kelmarsh Spa Resort</title>
<link href="https://fonts.googleapis.com/css2?family=Carlito:wght@400;700&display=swap" rel="stylesheet">
<style>
  :root {
    --sand: #e9e4dd;
    --page: #eff2f5;
    --rule: #2a2a2a;
    --ink: #111111;
    --muted: #8a8a8a;
    --stay: #e05a10;
    --soak: #1f9b52;
    --savour: #5a4016;
    --soothe: #d8bf8a;
    --leaf: #5cc41a;
    --active: #6aa312;
    --blue-dark: #1b6fc4;
    --link: #3a8fd0;
    --box-line: #8c8c8c;
  }
  * { box-sizing: border-box; margin: 0; padding: 0; }
  html, body { width: 1200px; height: 900px; overflow: hidden; }
  body {
    position: relative;
    background: var(--sand);
    font-family: "Carlito", "Calibri", sans-serif;
    color: var(--ink);
  }
  .page-band {
    position: absolute; left: 0; top: 201px; width: 1200px; height: 602px;
    background: var(--page);
    border-top: 1px solid var(--rule);
    border-bottom: 1px solid var(--rule);
  }
  .brand-name {
    position: absolute; left: 168px; top: 117px;
    font-size: 27px; font-weight: 400; color: var(--ink); line-height: 32px;
  }

  .section-nav { position: absolute; left: 177px; top: 169px; display: flex; gap: 3px; }
  .section-nav a {
    display: block; width: 149px; padding-top: 6px;
    border-top: 3px solid; text-align: center;
    font-size: 16px; letter-spacing: 1.2px; color: var(--ink); text-decoration: none;
  }
  .section-nav .stay { border-color: var(--stay); }
  .section-nav .soak { border-color: var(--soak); }
  .section-nav .savour { border-color: var(--savour); }
  .section-nav .soothe { border-color: var(--soothe); }

  .search {
    position: absolute; left: 1007px; top: 181px;
    display: flex; align-items: center; gap: 8px;
    color: var(--muted); font-size: 15px; letter-spacing: 0.8px;
  }
  .quick-actions { position: absolute; left: 920px; top: 202px; display: flex; gap: 1px; }
  .quick-actions a {
    display: block; width: 83px; height: 24px; line-height: 20px; text-align: center;
    background: linear-gradient(#1f8ad8, #3ea3ea 70%, #a8d4f3);
    color: #fff; font-size: 14px; text-decoration: none;
  }

  .side-nav { position: absolute; left: 86px; top: 231px; list-style: none; }
  .side-nav > li { font-size: 16px; line-height: 23.5px; padding-left: 16px; position: relative; letter-spacing: 0.3px; }
  .side-nav > li::before {
    content: ""; position: absolute; left: 1px; top: 6px;
    border-left: 6px solid var(--leaf); border-top: 5px solid transparent; border-bottom: 5px solid transparent;
  }
  .side-nav .sub { list-style: none; margin: 2px 0 9px 10px; }
  .side-nav .sub li { font-size: 14px; line-height: 20px; }
  .side-nav .sub li::before { display: none; }
  .side-nav .sub .current { color: var(--active); }

  .contact-card {
    position: absolute; left: 87px; top: 617px; width: 168px; height: 165px;
    border: 1px solid var(--box-line); border-radius: 9px;
    text-align: center; font-size: 14px; line-height: 15px; padding-top: 14px;
    font-style: normal; white-space: nowrap;
  }
  .contact-card strong { font-weight: 700; }
  .contact-card .gap { height: 15px; }
  .contact-card .email { color: var(--active); font-weight: 700; margin-top: 15px; display: block; }

  .content { position: absolute; left: 324px; top: 216px; width: 420px; }
  .content h1 { font-size: 28px; font-weight: 400; letter-spacing: 1px; line-height: 34px; }
  .content p { font-size: 12px; line-height: 18.9px; margin-top: 22px; white-space: nowrap; }
  .content p + p { margin-top: 19px; }
  .content ul { list-style: none; margin: 18px 0 0 29px; }
  .content li { font-size: 12px; line-height: 20.8px; position: relative; padding-left: 20px; }
  .content li::before {
    content: ""; position: absolute; left: 0; top: 8px;
    width: 5px; height: 5px; border-radius: 50%; background: var(--link);
  }
  .book-button {
    position: absolute; left: 326px; top: 753px; width: 114px; height: 30px;
    border-radius: 6px; background: linear-gradient(#5fa2e8, var(--blue-dark));
    color: #fff; font-size: 17px; text-align: center; line-height: 30px; text-decoration: none; letter-spacing: 0.4px;
  }

  .gallery { position: absolute; left: 882px; top: 282px; width: 206px; }
  .gallery .photo { display: block; }
  .photo-garden { width: 205px; height: 154px; background: linear-gradient(160deg, #3c5a34, #6f9a3c 55%, #4f8a28); }
  .photo-pool { width: 206px; height: 146px; margin-top: 3px; background: linear-gradient(#2f7a63, #3fae8e 60%, #1e8a5c); }
  .photo-room { width: 206px; height: 145px; margin-top: 12px; background: linear-gradient(135deg, #e8e6ea, #b9b2b4 55%, #d7d2d6); }
  .more-pictures {
    display: block; text-align: center; margin-top: 8px;
    color: var(--link); font-size: 13px; letter-spacing: 0.8px; text-decoration: none;
  }

  .footer-links {
    position: absolute; left: 85px; top: 806px; display: flex;
    font-size: 10px; letter-spacing: 1px; list-style: none;
  }
  .footer-links li + li::before { content: "|"; padding: 0 14px 0 16px; }
</style>
</head>
<body>
  <div class="page-band"></div>

  <header>
    <div class="brand-name">Taupo Kelmarsh</div>
    <nav class="section-nav">
      <a class="stay" href="#">stay</a>
      <a class="soak" href="#">soak</a>
      <a class="savour" href="#">savour</a>
      <a class="soothe" href="#">soothe</a>
    </nav>
    <div class="search">
      <svg width="13" height="13" viewBox="0 0 13 13" aria-hidden="true">
        <circle cx="8" cy="5" r="4" fill="none" stroke="#9a9a9a" stroke-width="1.2"/>
        <line x1="5" y1="8" x2="1" y2="12" stroke="#9a9a9a" stroke-width="1.4"/>
      </svg>
      <span>search</span>
    </div>
    <div class="quick-actions">
      <a href="#">book now</a>
      <a href="#">top deals</a>
    </div>
  </header>

  <ul class="side-nav">
    <li>Home</li>
    <li>Facilities
      <ul class="sub">
        <li>Holiday Park</li>
        <li>Luxury Accommodation</li>
        <li class="current">Family Accommodation</li>
        <li>Living Water Spa</li>
        <li>Hot Springs</li>
        <li>Cafe</li>
        <li>Info Centre</li>
        <li>Kids’ Activities</li>
      </ul>
    </li>
    <li>About</li>
    <li>Gallery</li>
    <li>Taupo</li>
    <li>Contact&nbsp; us</li>
  </ul>

  <address class="contact-card">
    <strong>Taupo&nbsp; Kelmarsh</strong><br>
    Kelmarsh&nbsp; Ridge&nbsp; Road<br>
    Lake&nbsp; Taupo
    <div class="gap"></div>
    New&nbsp; Yealand<br>
    phone:&nbsp; +64&nbsp; 7&nbsp; 555&nbsp; 0142<br>
    fax:&nbsp; +64&nbsp; 7&nbsp; 555&nbsp; 0187
    <span class="email">info@taupokelmarsh.com</span>
  </address>

  <main class="content">
    <h1>Family&nbsp; Accommodation</h1>
    <p>"Lorem ipsum dolor sit amet, consectetur adipisicing elit, sed do eiusmod<br>
    tempor incididunt ut labore et dolore magna aliqua. Ut enim ad minim<br>
    veniam, quis nostrud exercitation ullamco laboris nisi ut aliquip ex ea<br>
    commodo consequat. Duis aute irure dolor in reprehenderit in voluptate<br>
    velit esse cillum dolore eu fugiat nulla pariatur. Excepteur sint occaecat<br>
    &nbsp;cupidatat non proident, sunt in culpa qui officia deserunt mollit anim id<br>
    est laborum."</p>
    <p>"Lorem ipsum dolor sit amet, consectetur adipisicing elit, sed do eiusmod<br>
    tempor incididunt ut labore et dolore magna aliqua. Ut enim ad minim<br>
    veniam, quis nostrud exercitation ullamco laboris nisi ut aliquip ex ea<br>
    commodo consequat. Duis aute irure dolor in reprehenderit in voluptate<br>
    velit esse cillum dolore eu fugiat nulla pariatur. Excepteur sint occaecat<br>
    &nbsp;cupidatat non proident, sunt in culpa qui officia deserunt mollit anim id<br>
    est laborum."</p>
    <ul>
      <li>Lorem ipsum dolor sit amet, consectetur</li>
      <li>adipisicing elit, sed do eiusmod</li>
      <li>tempor incididunt ut labore et dolore</li>
      <li>magna aliqua. Ut enim ad minim</li>
      <li>veniam, quis nostrud exercitation ullamco</li>
      <li>laboris nisi ut aliquip ex ea</li>
    </ul>
  </main>
  <a class="book-button" href="#">book now</a>

  <aside class="gallery">
    <div class="photo photo-garden" role="img" aria-label="Photo of a family chalet with garden steps and lush green lawn"></div>
    <div class="photo photo-pool" role="img" aria-label="Photo of a group of friends relaxing in a green hot spring pool"></div>
    <div class="photo photo-room" role="img" aria-label="Photo of a guest using a laptop on a bed in a bright room"></div>
    <a class="more-pictures" href="#">show&nbsp; more&nbsp; pictures</a>
  </aside>

  <ul class="footer-links">
    <li>Home</li>
    <li>Privacz</li>
    <li>Site&nbsp; map</li>
    <li>Links</li>
    <li>Subscribe</li>
    <li>About&nbsp; us</li>
  </ul>
</body>
</html>
```